Office Building Banner

Need a 4x8 vinyl banner made for our office/storage headquarters. Our branded colors and logo can be taken from our website, www.halvenroofingtx.com. All other elements of our brand have not been decided on yet, so you have creative autonomy there. Our location faces a busy highway in Seguin, Texas, so the banner needs to have our contact information and full name clearly seen from a bit away's away, hope that makes sense. Our company wants to convey attributes of strength, loyalty, protection - basically emulating the qualities of a wolf and his pack. I have uploaded a few items we have been using to date, but as you can see, graphic design is not our forte.

```html
<!DOCTYPE html>
<html lang="en">
<head>
<meta charset="utf-8">
<title>Halven Roofing &amp; Renovations – Banner</title>
<link rel="stylesheet" href="https://fonts.googleapis.com/css2?family=Poppins:wght@400;700;800&display=swap">
<style>
  :root {
    --ink: #0a0a0a;
    --panel-black: #070707;
    --brand-orange: #f4811f;
    --orange-deep: #de6a1c;
    --paper: #ffffff;
    --text-dark: #1b1b1b;
  }
  html, body {
    margin: 0;
    padding: 0;
    width: 1200px;
    height: 741px;
    overflow: hidden;
    background: var(--paper);
  }
  .banner {
    position: relative;
    width: 1200px;
    height: 741px;
    background: var(--panel-black);
    font-family: "Poppins", sans-serif;
    overflow: hidden;
  }
  .banner-shapes {
    position: absolute;
    inset: 0;
  }
  .headline {
    position: absolute;
    left: 58px;
    top: 90px;
    margin: 0;
    font-weight: 800;
    font-size: 58px;
    line-height: 1.22;
    color: var(--paper);
  }
  .headline .accent { color: var(--brand-orange); }
  .values {
    position: absolute;
    left: 40px;
    top: 385px;
    display: flex;
    align-items: flex-end;
  }
  .value {
    width: 190px;
    display: flex;
    flex-direction: column;
    align-items: center;
    gap: 28px;
  }
  .value-divider {
    width: 3px;
    height: 200px;
    background: var(--brand-orange);
    align-self: center;
  }
  .value-icon-placeholder {
    width: 110px;
    height: 120px;
    border-radius: 18px;
    background: linear-gradient(160deg, rgba(244,129,31,0.55), rgba(244,129,31,0.25));
  }
  .value-label {
    font-weight: 400;
    font-size: 34px;
    color: var(--paper);
  }
  .brand {
    position: absolute;
    left: 760px;
    top: 110px;
    width: 400px;
    display: flex;
    align-items: center;
    gap: 18px;
  }
  .brand-dot {
    flex: none;
    width: 70px;
    height: 70px;
    border-radius: 50%;
    background: var(--ink);
  }
  .brand-name {
    font-weight: 800;
    font-size: 42px;
    line-height: 1.05;
    color: var(--ink);
  }
  .address {
    position: absolute;
    left: 740px;
    top: 380px;
    width: 440px;
    margin: 0;
    text-align: center;
    font-weight: 700;
    font-size: 30px;
    line-height: 1.25;
    color: var(--paper);
    font-style: normal;
  }
  .contact {
    position: absolute;
    left: 700px;
    top: 560px;
    width: 480px;
    text-align: center;
    color: var(--text-dark);
  }
  .phone {
    display: block;
    font-weight: 800;
    font-size: 64px;
    line-height: 1.05;
    letter-spacing: 1px;
  }
  .website {
    display: block;
    font-weight: 700;
    font-size: 31px;
  }
</style>
</head>
<body>
<main class="banner">
  <svg class="banner-shapes" width="1200" height="741" viewBox="0 0 1200 741" aria-hidden="true">
    <defs>
      <linearGradient id="chevron-shade" x1="0" x2="1" y1="0" y2="0">
        <stop offset="0" stop-color="#070707"/>
        <stop offset="1" stop-color="#2a211b"/>
      </linearGradient>
    </defs>
    <polygon points="560,120 620,120 660,520 600,741 540,741 600,520" fill="url(#chevron-shade)" opacity="0.6"/>
    <polygon points="600,60 650,60 700,520 640,741 590,741 650,520" fill="url(#chevron-shade)" opacity="0.8"/>
    <polygon points="630,0 1200,0 1200,520 712,520" fill="var(--orange-deep)"/>
    <polygon points="665,0 1200,0 1200,520 742,520" fill="var(--brand-orange)"/>
    <polygon points="712,520 1200,520 1200,741 640,741" fill="var(--paper)"/>
  </svg>

  <h1 class="headline">
    <span class="accent">Local Roofing</span><br>
    Company Serving<br>
    Greater, TX
  </h1>

  <section class="values">
    <div class="value">
      <div class="value-icon-placeholder" role="img" aria-label="Orange line icon of a flexed arm for strength"></div>
      <span class="value-label">Strength</span>
    </div>
    <div class="value-divider"></div>
    <div class="value">
      <div class="value-icon-placeholder" role="img" aria-label="Orange line icon of clasped hands under stars for loyalty"></div>
      <span class="value-label">Loyalty</span>
    </div>
    <div class="value-divider"></div>
    <div class="value">
      <div class="value-icon-placeholder" role="img" aria-label="Orange line icon of a shield for protection"></div>
      <span class="value-label">Protection</span>
    </div>
  </section>

  <div class="brand">
    <span class="brand-dot"></span>
    <span class="brand-name">Halven Roofing &amp; Renovations LLC</span>
  </div>

  <address class="address">P.O. Box 5318 Seguin<br>TX 78155</address>

  <div class="contact">
    <span class="phone">512-555-0186</span>
    <span class="website">www.halvenroofingtx.com</span>
  </div>
</main>
</body>
</html>
```